terras letterhead

We would like to create a new letterhead that our company will use for proposals, invoices, statements and letters. Our company name is Terra-Crafters. We are a landscape design/build and landscape maintenance company. We have a web site Terra-Crafters.example where our logo (the leaf with the lettering within it only) is displayed.

Industry/Entity Type

Graphic Design

Requirements
Must have
• Address and info on our current letterhead (uploaded)
Nice to have
• We would like the design to look presentable in grey scale as well as color.
Should not have
• Do not want to infringe much on the normal useable area within the normal print areas.

```html
<!DOCTYPE html>
<html lang="en">
<head>
<meta charset="utf-8">
<title>Terra-Crafters Letterhead</title>
<link href="https://fonts.googleapis.com/css2?family=Lato:wght@400;700&display=swap" rel="stylesheet">
<style>
  :root {
    --backdrop: #e4e4e4;
    --paper: #ffffff;
    --leaf-tint: #e6ece8;
    --leaf-soft: #f1f4f2;
    --brand-green: #2f6b45;
    --ink: #4a4a4a;
  }
  html, body {
    margin: 0;
    padding: 0;
    width: 1200px;
    height: 1000px;
    overflow: hidden;
    background: var(--backdrop);
  }
  .canvas {
    position: relative;
    width: 1200px;
    height: 1000px;
  }
  .letterhead {
    position: absolute;
    left: 252px;
    top: 50px;
    width: 696px;
    height: 900px;
    background: var(--paper);
    box-shadow: 2px 3px 6px rgba(0,0,0,0.35);
    overflow: hidden;
  }
  .foliage-art {
    position: absolute;
    left: 0;
    top: 30px;
    width: 696px;
    height: 680px;
    background:
      radial-gradient(ellipse 55% 45% at 62% 62%, var(--leaf-tint) 0%, var(--leaf-soft) 55%, rgba(255,255,255,0) 100%),
      radial-gradient(ellipse 20% 30% at 90% 20%, var(--leaf-soft) 0%, rgba(255,255,255,0) 100%);
  }
  .letterhead-footer {
    position: absolute;
    left: 22px;
    right: 30px;
    bottom: 34px;
    display: flex;
    align-items: center;
    justify-content: space-between;
    font-family: "Lato", sans-serif;
  }
  .brand {
    display: flex;
    align-items: center;
    gap: 6px;
    color: var(--brand-green);
    font-size: 13px;
    font-weight: 700;
    letter-spacing: 0.5px;
    text-transform: uppercase;
    white-space: nowrap;
  }
  .brand-dot {
    width: 10px;
    height: 10px;
    border-radius: 50%;
    background: var(--brand-green);
  }
  .contact {
    text-align: right;
    color: var(--ink);
    font-size: 8.5px;
    line-height: 1.35;
    white-space: nowrap;
  }
</style>
</head>
<body>
  <main class="canvas">
    <section class="letterhead">
      <div class="foliage-art" role="img" aria-label="Faint pale green illustration of large drifting leaves across the page"></div>
      <footer class="letterhead-footer">
        <div class="brand"><span class="brand-dot"></span><span class="brand-name">Terra-Crafters</span></div>
        <div class="contact">
          <div>1850 Meadowbrook Avenue Fairview, OR 97000 | Ph: (555) 010 -2468 &nbsp;| Fax: (555) 010 - 3579</div>
          <div>service@terra-crafters.example | www.terra-crafters.example</div>
        </div>
      </footer>
    </section>
  </main>
</body>
</html>
```